Invitation Design Project

This is an invitation to fit in a standard size envelope (#10 in Canada, 9 1/2 inches x 4 inches). This invitation is intended for potential major donors. There are already set branding guidelines for our logo which are attached.

Deliverables: A print ready invitation and a PDF for an attachment to email invitations.
Updates

Hi Designers,

I just updated the text for the bios.

Thanks for submitting to this project.

Kind regards,
Marika

Hello designers,

I have also uploaded the Prairiefest2013 Logos for your use.

Thanks!

Target Market(s)

Potential Major donors

Requirements
Must have
• The Beacon Canada logo. See attached.

To include on the invitation:

Please join us to hear about Prairiefest2013

Guest Speakers: Peter Holloway, President of Keelstone Corporation Vancouver
Marika Dunholt, National Director, Beacon Canada

Hosted by:
Ray Pemberton, President of Riverbend Alliance
Neil Farrow, Chairman, Ravenport Group Inc.
Bert Ostrand, Q.C.

Feb. 26, 2013 at 12 noon - 1:30 p.m.
The Ashwick Club
418 - 17 Ave SW, Calgary

R.S.V.P. to Nora Pelham npelham@riverbendalliance.example

Bio's on backside of invitation:

Peter Holloway is a founding principal of the Keelstone real estate organization based in Vancouver, Canada with offices in Atlanta, GA and Sacramento, CA. Since 1976, Keelstone has acquired, developed and financed a diversified portfolio of real estate assets in the residential and commercial sectors throughout North America. Peter Holloway is involved in a number of local and international charitable and community organizations most notably in his work with Beacon Canada, Beacon International,the Roofbridge Foundation and the Harwell Foundation. He graduated from the University of Westmarch with a Bachelor of Commerce degree and a Bachelor of Laws degree. He resides in Vancouver, Canada and is married to his wife Miriam (29 years); they have three children.
Marika Dunholt has been living and working in Vancouver for the last 15 years. Most of those years Marika helped women investigate their own spiritual lives through her work with Hearts at the Helm and then Beacon in the Workplace. Currently Marika is the National Director of Beacon Canada. She is married to Owen Dunholt, a Lakeside Constabulary Officer on the K9 Unit. Marika and Owen have two four legged family members, Pepper and Tumbler.

```html
<!DOCTYPE html>
<html lang="en">
<head>
<meta charset="utf-8">
<title>Guest Speaker Bios</title>
<link rel="stylesheet" href="https://fonts.googleapis.com/css2?family=Cabin:wght@600&display=swap">
<style>
  :root {
    --navy: #1f3f7c;
    --orange: #e3844c;
    --white: #ffffff;
    --paper-light: #f1f3f6;
    --paper-mid: #dfe4ea;
    --photo-warm: #b89478;
    --photo-cool: #6f6a66;
  }
  html, body {
    margin: 0;
    padding: 0;
    width: 1200px;
    height: 3086px;
    overflow: hidden;
  }
  .card {
    position: relative;
    width: 1200px;
    height: 3086px;
    overflow: hidden;
    background: radial-gradient(ellipse at 50% 45%, var(--paper-light) 0%, var(--paper-mid) 100%);
    font-family: "Cabin", "Myriad Pro", Arial, sans-serif;
    font-weight: 600;
    color: var(--navy);
  }
  .band {
    position: absolute;
    left: 0;
    width: 1200px;
  }
  .band-top { top: 0; height: 330px; }
  .band-bottom { bottom: 0; height: 420px; }

  .bio {
    position: absolute;
    left: 248px;
    width: 852px;
    margin: 0;
    font-size: 40px;
    line-height: 52px;
  }
  .bio-holloway { top: 660px; }
  .bio-dunholt { top: 1960px; }

  .portrait {
    float: left;
    margin-right: 14px;
    border-radius: 4px;
  }
  .portrait-holloway {
    width: 357px;
    height: 390px;
    margin-top: -240px;
    background: linear-gradient(160deg, var(--photo-warm) 0%, #8c7466 60%, #4c4f5a 100%);
  }
  .portrait-dunholt {
    width: 300px;
    height: 345px;
    margin-top: -65px;
    background: linear-gradient(160deg, #c9a48c 0%, var(--photo-cool) 55%, #3b3a3d 100%);
  }
</style>
</head>
<body>
<main class="card">
  <svg class="band band-top" viewBox="0 0 1200 330" aria-hidden="true">
    <path d="M470 0 C720 40 960 110 1200 230 L1200 330 C960 200 700 90 420 0 Z" fill="var(--white)"/>
    <path d="M520 0 C760 30 990 100 1200 190 L1200 250 C980 140 730 50 470 0 Z" fill="var(--orange)"/>
    <path d="M600 0 C800 20 1010 70 1200 150 L1200 185 C990 95 770 30 540 0 Z" fill="var(--white)"/>
    <path d="M640 0 L1200 0 L1200 140 C1020 60 830 15 640 0 Z" fill="var(--navy)"/>
  </svg>

  <article class="bio bio-holloway">
    <div class="portrait portrait-holloway" role="img" aria-label="Portrait photo of Peter Holloway"></div>
    Peter Holloway is a founding principal of the Keelstone real estate organization based in Vancouver, Canada with offices in Atlanta, GA and Sacramento, CA. Since 1976, Keelstone has acquired, developed and financed a diversified portfolio of real estate assets in the residential and commercial sectors throughout North America. Peter Holloway is involved in a number of local and international charitable and community organizations most notably in his work with Beacon Canada, Beacon International,the Roofbridge Foundation and the Harwell Foundation. He graduated from the University of Westmarch with a Bachelor of Commerce degree and a Bachelor of Laws degree. He resides in Vancouver, Canada and is married to his wife Miriam (29 years); they have three children.
  </article>

  <article class="bio bio-dunholt">
    <div class="portrait portrait-dunholt" role="img" aria-label="Portrait photo of Marika Dunholt"></div>
    Marika Dunholt has been living and working in Vancouver for the last 15 years. Most of those years Marika helped women investigate their own spiritual lives through her work with Hearts at the Helm and then Beacon in the Workplace. Currently Marika is the National Director of Beacon Canada. She is married to Owen Dunholt, a Lakeside Constabulary Officer on the K9 Unit. Marika and Owen have two four legged family members, Pepper and Tumbler.
  </article>

  <svg class="band band-bottom" viewBox="0 0 1200 420" aria-hidden="true">
    <path d="M0 40 C300 10 620 80 1200 210 L1200 420 L0 420 Z" fill="var(--navy)"/>
    <path d="M0 95 C320 70 640 140 1200 270 L1200 420 L0 420 Z" fill="var(--white)"/>
    <path d="M0 140 C330 120 660 200 1200 330 L1200 420 L0 420 Z" fill="var(--orange)"/>
    <path d="M0 250 C300 240 600 310 900 420 L0 420 Z" fill="var(--white)"/>
    <path d="M0 290 C280 285 540 340 780 420 L0 420 Z" fill="var(--navy)"/>
  </svg>
</main>
</body>
</html>
```